Book Cover Design Project

Hello,

I am looking to get a cover created for my book.

Size 6 X 9

Title:
Quiet Ledger Steady Gains

Sub-Title:
Plain Methods for Growing Steady Gains Within Your Quiet Ledger

Author:
Martin Fenwick

The book could have an image or only typography.

If it does include an image do not use an image of a real person. If you use a person, he can be shaded in, outlined, etc

I like the color white and blue however, I am open to other colors as well.

Below is the cover of my previous book that has an image:
http://www.quillmarket.example/Dawn-Of-Stag-Path-Vowed-Final/dp/284610375K/ref=sr_1_1?ie=UTF8&s=books&qid=2417307529&sr=1-1

I like simple designs but open to other concepts also

attached is the text to be used for the back of the book.

Thank you in advance for your designs,

Target Market(s)

This book will be for small business owners. Typically males/females between the age of 25 - 45 looking to make more money without going broke with marketing.

Industry/Entity Type

Business

Requirements
Must have
• Must include the Title, Subtitle and Author on the cover

Nice to have
• An image that represents a small business growing
Should not have
• Images of a real person. Stylized versions are ok.

```html
<!DOCTYPE html>
<html lang="en">
<head>
<meta charset="utf-8">
<title>Quiet Ledger Steady Gains – Book Cover</title>
<link rel="stylesheet" href="https://fonts.googleapis.com/css2?family=PT+Sans:wght@400;700&family=PT+Sans+Narrow:wght@400;700&family=PT+Serif&display=swap">
<style>
  :root {
    --page-bg: #e4e5e7;
    --paper: #ffffff;
    --brand-blue: #1d5aa6;
    --link-blue: #2a63b8;
    --ink: #1f1f1f;
    --art-light: #dbe4fb;
    --art-mid: #6f86e8;
  }
  * { margin: 0; padding: 0; box-sizing: border-box; }
  html, body { width: 1200px; height: 882px; overflow: hidden; background: var(--page-bg); }
  .canvas { position: relative; width: 1200px; height: 882px; }

  .spread {
    position: absolute; left: 27px; top: 22px; width: 1150px; height: 839px;
    background: var(--paper);
    box-shadow: 0 1px 3px rgba(0,0,0,.15);
  }

  /* Back cover */
  .back-cover { position: absolute; left: 0; top: 0; width: 556px; height: 839px;
    font-family: "PT Sans", sans-serif; color: var(--ink); }
  .back-headline { position: absolute; left: 34px; top: 24px; width: 420px;
    font-weight: 700; font-size: 23.5px; line-height: 34px; color: var(--brand-blue); }
  .back-headline span { display: block; padding-left: 11px; }
  .back-headline span:first-child { padding-left: 0; }
  .back-body { position: absolute; left: 46px; top: 190px; width: 432px;
    font-size: 14.3px; line-height: 19.5px; }
  .back-body p { margin-bottom: 19.5px; }
  .back-body .lead-in { padding-left: 4px; margin-bottom: 14px; }
  .benefits { list-style: none; color: var(--link-blue); margin-bottom: 19.5px; }
  .benefits li::before { content: "\2022\00a0"; }
  .about { position: absolute; left: 46px; top: 658px; width: 405px;
    font-size: 11.6px; line-height: 16px; }
  .about h2 { font-size: 11.6px; font-weight: 700; }
  .site-note { position: absolute; left: 46px; top: 795px; font-size: 11.6px; line-height: 16px; }
  .site-note a { color: var(--link-blue); }

  /* Spine */
  .spine { position: absolute; left: 556px; top: 0; width: 33px; height: 839px;
    background: linear-gradient(90deg, #f4f4f5 0%, #ffffff 40%, #ffffff 70%, #f1f1f2 100%); }
  .spine-shadow { position: absolute; left: 460px; top: 0; width: 96px; height: 839px;
    background: linear-gradient(90deg, rgba(0,0,0,0) 0%, rgba(0,0,0,.06) 100%); }
  .spine-shadow--front { left: 589px; width: 60px;
    background: linear-gradient(90deg, rgba(0,0,0,.07) 0%, rgba(0,0,0,0) 100%); }
  .spine-author, .spine-title { position: absolute; left: 50%; white-space: nowrap;
    transform-origin: center; color: var(--brand-blue); }
  .spine-author { top: 95px; font-family: "PT Serif", serif; font-size: 12.5px; color: var(--ink);
    transform: translate(-50%, -50%) rotate(90deg); }
  .spine-title { top: 440px; font-family: "PT Sans", sans-serif; font-size: 17px; letter-spacing: .3px;
    transform: translate(-50%, -50%) rotate(90deg); }
  .spine-title strong { font-weight: 700; }

  /* Front cover */
  .front-cover { position: absolute; left: 589px; top: 0; width: 561px; height: 839px;
    font-family: "PT Sans", sans-serif; text-align: center; }
  .copyright-mark { position: absolute; left: 0; width: 561px; font-size: 11.5px; font-weight: 700; color: var(--ink); }
  .copyright-mark--top { top: 28px; }
  .copyright-mark--bottom { top: 794px; }
  .cover-art { position: absolute; left: 15px; top: 58px; width: 540px; height: 430px; }
  .title { position: absolute; left: 0; top: 497px; width: 561px;
    font-family: "PT Sans Narrow", sans-serif; font-weight: 700; color: var(--brand-blue);
    line-height: 1; white-space: nowrap; }
  .title-top { display: block; font-size: 54px; letter-spacing: .5px; }
  .title-bottom { display: block; font-size: 90px; margin-top: 2px; letter-spacing: -.5px; }
  .subtitle { position: absolute; left: 0; top: 654px; width: 561px;
    font-size: 17.5px; font-weight: 700; line-height: 24px; color: var(--ink); }
  .author { position: absolute; left: 0; top: 722px; width: 561px;
    font-family: "PT Serif", serif; font-size: 25px; line-height: 32px; color: var(--brand-blue); }
</style>
</head>
<body>
<div class="canvas">
  <div class="spread">

    <section class="back-cover">
      <h1 class="back-headline">
        <span>“Dramatically Increase Your Sales</span>
        <span>And Revenue With Effective</span>
        <span>Marketing Strategies, Guaranteed</span>
        <span>To Get Results!"</span>
      </h1>
      <div class="back-body">
        <p>Are lackluster sales getting you down?</p>
        <p>Does it seem like — no matter how much testing and tweaking you do — you continue to struggle with getting new customers, creating a strong online and offline presence, and maximizing the lifetime value of existing customers, and now you're running out of time, patience... and money?</p>
        <p class="lead-in">What if I told you that I could help you:</p>
        <ul class="benefits">
          <li>Gain and retain new customers</li>
          <li>Get others to promote your business</li>
          <li>Make more money from your existing customers</li>
          <li>Get results that will blow your competition away</li>
        </ul>
        <p>... And I can show you how to do it FASTER, for a small fraction of what you'd pay in-house marketing employees to get the SAME results!</p>
        <p>Curious? Then open this book right now and I'll explain how it's done...</p>
      </div>
      <div class="about">
        <h2>About the Author:</h2>
        <p>Martin Fenwick is a partner of Harbor Lane Marketing, which helps small businesses get more customers by making them findable on the Internet. He is a best selling author and has a bachelor's degree in Internet Marketing. He dedicates his time to learning as much as possible, both in marketing and in life.</p>
      </div>
      <p class="site-note">See how he can serve your business by going to<br><a href="#">www.harborlanemarketing.example</a></p>
      <div class="spine-shadow"></div>
    </section>

    <div class="spine">
      <span class="spine-author">by Martin Fenwick</span>
      <span class="spine-title">QUIET LEDGER <strong>STEADY GAINS</strong></span>
    </div>
    <div class="spine-shadow spine-shadow--front"></div>

    <section class="front-cover">
      <p class="copyright-mark copyright-mark--top">Copyrighted Material</p>
      <svg class="cover-art" viewBox="0 0 540 430" role="img" aria-label="Illustration: blue figures pushing a rising growth arrow upward">
        <defs>
          <radialGradient id="artGlow" cx="62%" cy="55%" r="60%">
            <stop offset="0%" stop-color="var(--art-mid)" stop-opacity=".75"/>
            <stop offset="55%" stop-color="var(--art-light)" stop-opacity=".7"/>
            <stop offset="100%" stop-color="#ffffff" stop-opacity="0"/>
          </radialGradient>
        </defs>
        <rect width="540" height="430" fill="url(#artGlow)"/>
      </svg>
      <h2 class="title">
        <span class="title-top">QUIET LEDGER</span>
        <span class="title-bottom">STEADY GAINS</span>
      </h2>
      <p class="subtitle">Plain Methods for Growing Steady Gains<br>Within Your Quiet Ledger</p>
      <p class="author">by Martin Fenwick</p>
      <p class="copyright-mark copyright-mark--bottom">Copyrighted Material</p>
    </section>

  </div>
</div>
</body>
</html>
```